High end personal training flyer design

I want a flyer designed to be delivered to people's houses to interest them in high end (and, therefore, not cheap) personal training services.

Don't want standard pictures of people exercising, before and afters, etc. More something that will appeal to that more affluent market.

Flexible on size of flyer, but please make sure it is a standard size that I can get printed easily. Would like it not to look like a normal flyer you get through the letterbox, so if any particular sizes, shapes, etc are known to do that, then that would be a good start.

Text on flyer to be as follows:

Is this you:

Live in East Cheshire
Male, aged 30-50
A father
Cash rich, time poor
Find handling high pressure at work comfortable
But have a short fuse out of work – with the wife, kids, life in general, etc
Not happy with the way your body looks and feels
Know exactly what you should do to sort that, but struggling to actually do it for various reasons
Turned off by the standard menu of options for addressing that – gyms, slimming clubs, diets, etc

If so, you may be interested in what I do.

Some would call it Personal Training. Some would call it Coaching. I’m not interested in giving what I do labels.

What I am interested in is providing the best possible service (and results) for my clients – whatever that entails.

I work closely with one or two clients at a time to make sure they get exactly what they need.

If you would like to find out more about this, I usually meet for a coffee and a chat. To see if we both think our working together is a good idea.

No squeeze pages, no countdowns, mailing lists or false scarcity.

No plastering this flyer with ‘Before and afters’ – they are ten a penny and my clients don’t want to have pictures of them in their underwear spread around the local area.

Just give me a call and we’ll go from there.

My number is 07912645320.

Tim

Industry/Entity Type

Training

Requirements
Should not have
• Generic before and after or exercise type pictures

```html
<!DOCTYPE html>
<html lang="en">
<head>
<meta charset="utf-8">
<title>Is this you? – Personal Training Flyer</title>
<link href="https://fonts.googleapis.com/css2?family=Oswald:wght@300;400&family=Open+Sans:wght@400;600;700&display=swap" rel="stylesheet">
<style>
  :root {
    --backdrop: #2a2a2a;
    --paper: #ece3e1;
    --band: #5b5c5e;
    --band-edge: #cfcccc;
    --title: #7c7e82;
    --ink: #2b2b2b;
    --panel: #ffffff;
    --frame: #ffffff;
    --photo-light: #e9ebee;
    --photo-mid: #b9bcc2;
    --photo-dark: #6c7079;
  }
  * { box-sizing: border-box; margin: 0; padding: 0; }
  html, body {
    width: 1200px; height: 1200px; overflow: hidden;
    background: var(--backdrop);
  }
  .flyer {
    position: absolute; left: 160px; top: 40px;
    width: 880px; height: 1120px;
    background: var(--paper);
    box-shadow: 0 10px 30px rgba(0,0,0,.5);
    overflow: hidden;
    font-family: "Open Sans", Arial, sans-serif;
    color: var(--ink);
  }
  .side-band {
    position: absolute; left: 0; top: 0; bottom: 0; width: 210px;
    background: var(--band);
    border-right: 6px solid var(--band-edge);
  }
  .snapshot {
    position: absolute; width: 212px; height: 190px;
    background: var(--frame); border-radius: 8px; padding: 14px;
    box-shadow: 3px 5px 12px rgba(0,0,0,.35);
  }
  .snapshot .photo {
    width: 100%; height: 100%;
    background: linear-gradient(135deg, var(--photo-light) 0%, var(--photo-mid) 60%, var(--photo-dark) 100%);
  }
  .snap-1 { left: 30px;  top: 85px;  transform: rotate(-2deg); }
  .snap-2 { left: 62px;  top: 285px; transform: rotate(-1deg); }
  .snap-3 { left: 50px;  top: 480px; transform: rotate(-2deg); }
  .snap-4 { left: 100px; top: 668px; transform: rotate(-1.5deg); }
  .snap-5 { left: 76px;  top: 872px; transform: rotate(-2deg); }

  .title {
    position: absolute; left: 292px; top: 38px;
    font-family: "Oswald", "Arial Narrow", sans-serif; font-weight: 400;
    font-size: 86px; line-height: 1; color: var(--title);
    letter-spacing: -1px;
  }
  .profile-panel {
    position: absolute; left: 292px; top: 160px;
    width: 505px; height: 372px;
    background: var(--panel); padding: 28px 26px;
  }
  .profile-panel h2 {
    font-size: 19px; font-weight: 700; margin-bottom: 8px;
  }
  .profile-tags {
    font-family: "Oswald", "Arial Narrow", sans-serif; font-weight: 400;
    font-size: 22px; margin-bottom: 12px;
  }
  .checklist { list-style: none; }
  .checklist li {
    position: relative; padding-left: 24px;
    font-size: 14.5px; line-height: 1.75; margin-bottom: 4px;
  }
  .checklist li::before {
    content: ""; position: absolute; left: 0; top: 6px;
    width: 11px; height: 11px; border: 1.5px solid var(--ink); border-radius: 50%;
  }
  .service-block {
    position: absolute; left: 330px; top: 548px; width: 490px;
  }
  .service-block h3 {
    font-family: "Oswald", "Arial Narrow", sans-serif; font-weight: 400;
    font-size: 25px; margin-bottom: 6px;
  }
  .call-line { display: flex; align-items: baseline; gap: 8px; }
  .phone {
    font-family: "Oswald", "Arial Narrow", sans-serif; font-weight: 400;
    font-size: 26px; line-height: 1;
  }
  .footer-photo {
    position: absolute; left: 216px; right: 0; bottom: 0; height: 310px;
    background: linear-gradient(180deg, rgba(236,227,225,1) 0%, #c9c7c8 45%, #a8a7a9 100%);
  }
</style>
</head>
<body>
  <div class="flyer">
    <div class="footer-photo" role="img" aria-label="Faded photo of two people in running shoes tying their laces on a paved path"></div>
    <div class="side-band"></div>

    <div class="snapshot snap-1"><div class="photo" role="img" aria-label="Tired businessman resting his head on his office desk"></div></div>
    <div class="snapshot snap-2"><div class="photo" role="img" aria-label="Stressed businessman with hands pressed together at his forehead"></div></div>
    <div class="snapshot snap-3"><div class="photo" role="img" aria-label="Businessman at his desk holding his aching lower back"></div></div>
    <div class="snapshot snap-4"><div class="photo" role="img" aria-label="Businessman rubbing his sore neck at his desk"></div></div>
    <div class="snapshot snap-5"><div class="photo" role="img" aria-label="Weary businessman leaning his head on his hand at his desk"></div></div>

    <h1 class="title">is this you ?</h1>

    <section class="profile-panel">
      <h2>Live in East Cheshire</h2>
      <p class="profile-tags">Male, aged 30-50 &nbsp;|&nbsp; A father &nbsp;|&nbsp; Cash rich, time poor</p>
      <ul class="checklist">
        <li>Find handling high pressure at work comfortable.</li>
        <li>But have a short fuse out of work –<br>with the wife, kids, life in general, etc.</li>
        <li>Not happy with the way your body looks and feels Know exactly what you should do to sort that, but struggling to actually do it for various reasons.</li>
        <li>Turned off by the standard menu of options for addressing that – gyms, slimming clubs, diets, etc.</li>
      </ul>
    </section>

    <section class="service-block">
      <h3>Rejuvenate your life</h3>
      <ul class="checklist">
        <li>If so, you may be interested in what I do.</li>
        <li>Some would call it Personal Training. Some would call it Coaching. I’m not interested in giving what I do labels.</li>
        <li>What I am interested in is providing the best possible service (and results) for my clients – whatever that entails.</li>
        <li>I work closely with one or two clients at a time to make sure they get exactly what they need.</li>
        <li>If you would like to find out more about this, I usually meet for a coffee and a chat. To see if we both think our working together is a good idea.</li>
        <li><span class="call-line">Just give me (<strong>Tim</strong>) a call <span class="phone">my number is 07912645320</span></span></li>
      </ul>
    </section>
  </div>
</body>
</html>
```